Business card for real estate agent / office

We're looking for a new business card. We want something that is pretty clean, modern and sleek. Something that also tells people that we are a new age company...cutting edge. Although real estate has been done a certain way the last 100 years, we have energy and vibrance. Company name is Silver Meadow Properties. info can be found here: http://www.smprealtyhub.example/

needs to include: Name, title, phone number, email. our license number also needs to be displayed somewhere.

Target Market(s)

25-55 homeowners or potential homeowners

Industry/Entity Type

Business

Contact Information for Business Card

we need business card designs for real estate agent / office

Font styles to use
Serif

Requirements
Must have
• needs to include: Name, title, phone number, email. our license number also needs to be displayed somewhere and company name.
Nice to have
• placement area for photo

```html
<!DOCTYPE html>
<html lang="en">
<head>
<meta charset="utf-8">
<title>Silver Meadow Properties – Business Card</title>
<link rel="stylesheet" href="https://fonts.googleapis.com/css2?family=Crimson+Pro:wght@400;600;700&display=swap">
<style>
  :root {
    --navy: #1f3c64;
    --green: #6bb33e;
    --ink: #2a2a2a;
    --card: #ffffff;
    --backdrop: #e9e9ea;
    --card-shadow: rgba(0, 0, 0, 0.12);
  }
  * { box-sizing: border-box; margin: 0; padding: 0; }
  html, body {
    width: 1200px;
    height: 533px;
    overflow: hidden;
  }
  body {
    background: var(--backdrop);
    font-family: "Crimson Pro", Georgia, serif;
    color: var(--ink);
    position: relative;
  }
  .card {
    position: absolute;
    top: 87px;
    width: 540px;
    height: 307px;
    background: var(--card);
    box-shadow: 0 2px 10px var(--card-shadow);
  }
  .card--front { left: 63px; }
  .card--back { left: 624px; }

  .brand {
    position: absolute;
    display: flex;
    flex-direction: column;
    align-items: center;
    gap: 8px;
    width: 180px;
    font-family: "Crimson Pro", Georgia, serif;
    font-weight: 700;
    font-size: 22px;
    line-height: 1.05;
    color: var(--navy);
    text-align: center;
  }
  .brand__mark {
    width: 14px;
    height: 14px;
    background: var(--green);
    flex: none;
  }
  .card--front .brand { left: 38px; top: 104px; }
  .card--back .brand { left: 166px; top: 106px; }

  .divider {
    position: absolute;
    left: 264px;
    top: 91px;
    width: 2px;
    height: 136px;
    background: var(--navy);
  }

  .person {
    position: absolute;
    left: 307px;
    top: 32px;
  }
  .person__name {
    font-weight: 600;
    font-size: 14px;
    color: var(--navy);
    line-height: 1.2;
  }
  .person__surname { color: var(--green); }
  .person__title {
    font-size: 9px;
    margin-top: 4px;
    color: var(--ink);
  }

  .contact {
    position: absolute;
    left: 307px;
    top: 106px;
    font-size: 9px;
    line-height: 1.45;
    color: var(--ink);
  }
  .contact__row {
    display: grid;
    grid-template-columns: 61px auto;
    margin-bottom: 12px;
  }
  .contact__row:last-child { margin-bottom: 0; }
  .contact__label { color: var(--navy); }
</style>
</head>
<body>
  <section class="card card--front" aria-label="Business card front">
    <div class="brand">
      <span class="brand__mark"></span>
      <span class="brand__name">Silver Meadow Properties</span>
    </div>
    <div class="divider"></div>
    <div class="person">
      <p class="person__name">Lauren <span class="person__surname">Whitfield</span></p>
      <p class="person__title">CEO</p>
    </div>
    <div class="contact">
      <div class="contact__row"><span class="contact__label">Phone</span><span>555-014-2287</span></div>
      <div class="contact__row"><span class="contact__label">Email</span><span>info@smprealtyhub.example</span></div>
      <div class="contact__row"><span class="contact__label">Website</span><span>http://www.smprealtyhub.example</span></div>
      <div class="contact__row"><span class="contact__label">Address</span><span>418 Harbor View Drive, Suite 902<br>Bayport, Texas 78990</span></div>
      <div class="contact__row"><span class="contact__label">License</span><span>TX #0584217</span></div>
    </div>
  </section>

  <section class="card card--back" aria-label="Business card back">
    <div class="brand">
      <span class="brand__mark"></span>
      <span class="brand__name">Silver Meadow Properties</span>
    </div>
  </section>
</body>
</html>
```